Simple, elegant, business card design required

Hi designers,I am looking for a simple yet elegant business card design.

Please make use of my logo (attached); you are free to tweak the logo should you wish to do so.

Our business is involved in many different fields - almost all of them involved in some form of "design", so that's really one of the key things I want to portray. I do not wish to specify which field of design, exactly.

I prefer white on black (or just monochromatic), but if you have a different, creative idea, I am open to that too.

You can use artsy photographs provided that you have the license to use those. Please feel free to ask me any questions.
Updates

Project Deadline Extended Reason: Small extension for potential revisions. Did not get the time to provide as much feedback as I can. Added Wednesday, July 09, 2014

Target Market(s)

High-end customers looking for design consultancy

Industry/Entity Type

Business

Contact Information for Business Card

Name: Gareth Moonfield
Position: Creative Director
Mobile: +155603928174
Address: Barrow Lane, Ashcombe upon Tarn, Wenlockshire GL12 4RT
Website: torvakest.com (not launched yet)

Requirements
Must have
• Design layout must be clean, original, and text must be readable when printed.
Should not have
• ~ No business card templates please. Anyone using this will be reported.
• ~ Please don't spam entries.

```html
<!DOCTYPE html>
<html lang="en">
<head>
<meta charset="utf-8">
<title>Torvakest – Business Card</title>
<link rel="stylesheet" href="https://fonts.googleapis.com/css2?family=Oswald:wght@300&family=Archivo+Narrow:wght@700&family=Crimson+Pro:wght@400&display=swap">
<style>
  :root {
    --page-bg: #ffffff;
    --card-grey: #b3b3b3;
    --card-grey-light: #bcbcbc;
    --card-grey-dark: #a9a9a9;
    --ink: #1e1b1c;
    --paper-white: #ffffff;
    --band-black: #221e1f;
  }
  * { box-sizing: border-box; margin: 0; padding: 0; }
  html, body {
    width: 1200px;
    height: 1000px;
    overflow: hidden;
    background: var(--page-bg);
  }
  .canvas {
    position: relative;
    width: 1200px;
    height: 1000px;
  }
  .business-card {
    position: absolute;
    left: 146px;
    top: 220px;
    width: 908px;
    height: 560px;
    overflow: hidden;
  }
  .card-texture {
    position: absolute;
    inset: 0;
    background: linear-gradient(135deg, var(--card-grey-light) 0%, var(--card-grey) 50%, var(--card-grey-dark) 100%);
  }
  .brand-name {
    position: absolute;
    left: 300px;
    width: 440px;
    top: 222px;
    text-align: center;
    font-family: "Oswald", sans-serif;
    font-weight: 300;
    font-size: 58px;
    letter-spacing: 0.34em;
    text-indent: 0.34em;
    color: var(--ink);
    line-height: 1;
    white-space: nowrap;
  }
  .person {
    position: absolute;
    left: 85px;
    width: 370px;
    top: 388px;
    text-align: center;
    font-family: "Archivo Narrow", sans-serif;
    font-weight: 700;
  }
  .person-name {
    font-size: 38px;
    color: var(--paper-white);
    text-shadow: 2px 3px 3px rgba(0,0,0,0.6);
    line-height: 1.1;
  }
  .person-role {
    margin-top: 6px;
    font-size: 30px;
    color: var(--ink);
    line-height: 1.1;
  }
  .divider {
    position: absolute;
    left: 487px;
    top: 328px;
    width: 14px;
    height: 180px;
  }
  .contact-list {
    position: absolute;
    left: 542px;
    top: 344px;
    list-style: none;
    font-family: "Crimson Pro", serif;
    font-size: 21px;
    color: var(--ink);
    line-height: 33px;
    white-space: nowrap;
  }
  .contact-list li { display: flex; }
  .contact-list .label {
    width: 36px;
    flex: none;
    color: var(--paper-white);
  }
  .contact-list .gap { margin-bottom: 5px; }
  .bottom-band {
    position: absolute;
    left: 0;
    right: 0;
    bottom: 0;
    height: 50px;
    background: var(--band-black);
  }
</style>
</head>
<body>
<main class="canvas">
  <section class="business-card">
    <div class="card-texture" role="img" aria-label="Embossed paper texture with a soft grid of rounded squares"></div>

    <h1 class="brand-name">TORVAKEST</h1>

    <div class="person">
      <p class="person-name">Gareth Moonfield</p>
      <p class="person-role">Creative Director</p>
    </div>

    <svg class="divider" viewBox="0 0 14 180" aria-hidden="true">
      <path d="M7 0 L10 90 L7 180 L4 90 Z" fill="var(--ink)"/>
    </svg>

    <ul class="contact-list">
      <li class="gap"><span class="label">M :</span><span>+155603928174</span></li>
      <li><span class="label">A :</span><span>Barrow Lane, Ashcombe upon Tarn,</span></li>
      <li class="gap"><span class="label"></span><span>Wenlockshire GL12 4RT</span></li>
      <li><span class="label">W :</span><span>torvakest.com</span></li>
    </ul>

    <div class="bottom-band"></div>
  </section>
</main>
</body>
</html>
```